Personal Injury Law Firm Needs a Flyer for display at Medical Facilities

***UPDATED: I Converted the photo from .CR2 to JPG because some designers had issues opening it.***

We need a flyer design to fit:

https://www.shopvarnel.com/gp/product/K7742QX9TR/ref=oh_aui_detailpage_o00_s00?ie=UTF8&psc=1

I believe that the dimensions for the flyer would be 4 inches wide by 8 inches tall.

We need the flyer to include:
*Our company logo (vector files attached [USE EITHER ONE, DEPENDING ON WHICH BETTER SUITS YOUR DESIGN!])
*Contact phone number: "(888) 514 - 2673"
*Contact email: "info@morvillelaw.com"
*Website: "Morvillelaw.com"
*The wording: "Injured in an accident? Unhappy with your attorney? We get RESULTS!"
*The wording: "With over 20 years experience"
*The wording: "Over millions recovered"
*The badges for "Prime Counsel", "Lexra 10.0", and "Grand-Verdict dollars barrister circle" (THESE ARE ON THE FRONT PAGE OF OUR WEBSITE (UNDER THE VIDEO), AND HIGHER RESOLUTIONS CAN BE FOUND ON FINDORA)

Industry/Entity Type

Law Firm

Font styles to use
Serif

Requirements
Must have
• We need the flyer to include:
• *Our company logo (vector files attached [USE EITHER ONE, DEPENDING ON WHICH BETTER SUITS YOUR DESIGN!])
• *Contact phone number: "(888) 514 - 2673"
• *Contact email: "info@morvillelaw.com"
• *Website: "Morvillelaw.com"
• *The wording: "Injured in an accident? Unhappy with your attorney? We get RESULTS!"
• *The wording: "With over 20 years experience"
• *The wording: "Over millions recovered"
• *The badges for "Prime Counsel", "Lexra 10.0", and "Grand-Verdict dollars barrister circle" (THESE ARE ON THE FRONT PAGE OF OUR WEBSITE (UNDER THE VIDEO), AND HIGHER RESOLUTIONS CAN BE FOUND ON FINDORA)

```html
<!DOCTYPE html>
<html lang="en">
<head>
<meta charset="utf-8">
<title>Morville Law – Personal Injury Flyer</title>
<link rel="stylesheet" href="https://fonts.googleapis.com/css2?family=Roboto+Condensed:wght@300;400;700&family=Lato:ital,wght@0,400;1,400&display=swap">
<style>
  :root {
    --navy: #2b3e58;
    --blue: #1ea7e4;
    --slate: #3d4145;
    --paper: #eef0f2;
    --white: #ffffff;
    --ink: #1c1c1c;
  }
  * { box-sizing: border-box; margin: 0; padding: 0; }
  html, body { width: 710px; height: 1200px; overflow: hidden; background: var(--white); }
  .flyer { position: relative; width: 710px; height: 1200px; overflow: hidden; font-family: "Roboto Condensed", Arial, sans-serif; }
  .meeting-photo {
    position: absolute; left: 0; top: 90px; width: 710px; height: 530px;
    background: linear-gradient(100deg, #2d3440 0%, #9aa3ad 22%, #e9edf1 45%, #dfe4e9 62%, #3a4150 85%, #2a3039 100%);
  }
  .shapes { position: absolute; inset: 0; }

  .brand { position: absolute; top: 30px; left: 0; width: 710px; text-align: center; }
  .brand-name { display: inline-flex; align-items: center; gap: 14px; font-family: "Lato", Arial, sans-serif; font-size: 32px; line-height: 1; color: var(--white); }
  .brand-mark { width: 38px; height: 38px; background: var(--blue); }
  .brand-tagline { margin-top: 12px; padding-left: 52px; font-family: "Lato", Arial, sans-serif; font-style: italic; font-size: 15px; color: #d9e2ec; }

  .experience { position: absolute; left: 26px; top: 614px; width: 236px; text-align: center; color: var(--navy); font-weight: 700; line-height: 1; }
  .experience .over { font-size: 38px; }
  .experience .years { font-size: 48px; color: var(--white); margin: 2px 0 4px; }
  .experience .label { font-size: 32px; }

  .headline { position: absolute; right: 28px; top: 652px; text-align: right; color: var(--navy); line-height: 0.88; font-size: 72px; }
  .headline .line-1 { font-weight: 700; }
  .headline .line-2 { font-weight: 300; }
  .headline .line-3 { font-weight: 300; color: var(--blue); }

  .results { position: absolute; left: 258px; top: 869px; width: 452px; height: 64px; background: var(--blue); color: var(--white); display: flex; align-items: center; justify-content: center; font-size: 50px; font-weight: 700; line-height: 1; }
  .results .caps { font-weight: 400; font-size: 44px; margin-left: 12px; }

  .recovered { position: absolute; left: 28px; top: 852px; width: 200px; text-align: center; color: var(--white); line-height: 1.02; }
  .recovered .small { font-size: 30px; font-weight: 700; }
  .recovered .big { font-size: 44px; }

  .contact { position: absolute; left: 28px; top: 988px; color: var(--white); line-height: 1; }
  .contact .cta { font-size: 40px; font-weight: 700; color: var(--blue); }
  .contact .phone { font-size: 28px; font-weight: 700; margin-top: 14px; }
  .contact .email { font-family: "Lato", Arial, sans-serif; font-size: 21px; margin-top: 14px; }

  .credentials { position: absolute; right: 64px; top: 970px; list-style: none; text-align: right; font-family: "Lato", Arial, sans-serif; font-size: 22px; color: var(--ink); line-height: 1.15; }
  .credentials li { position: relative; margin-bottom: 9px; }
  .credentials li::after { content: ""; position: absolute; right: -18px; top: 10px; width: 7px; height: 7px; border-radius: 50%; background: var(--blue); }

  .website { position: absolute; left: 0; bottom: 0; width: 710px; height: 60px; display: flex; align-items: center; justify-content: center; font-family: "Lato", Arial, sans-serif; font-size: 23px; letter-spacing: 8px; color: var(--white); }
</style>
</head>
<body>
<main class="flyer">
  <div class="meeting-photo" role="img" aria-label="Photo of four lawyers in business suits talking around a bright conference table"></div>

  <svg class="shapes" width="710" height="1200" viewBox="0 0 710 1200" xmlns="http://www.w3.org/2000/svg">
    <defs>
      <linearGradient id="paperTone" x1="0" y1="0" x2="1" y2="1">
        <stop offset="0" stop-color="#e4e7ea"/>
        <stop offset="1" stop-color="#f5f6f7"/>
      </linearGradient>
    </defs>
    <polygon points="0,0 710,0 710,104 465,173 0,104" fill="var(--navy)"/>
    <polygon points="0,104 465,173 710,104 710,118 465,187 0,118" fill="var(--blue)"/>
    <g role="img" aria-label="Faint background image of legal documents and a judge's gavel">
      <polygon points="0,636 477,567 710,624 710,1140 0,1140" fill="url(#paperTone)"/>
    </g>
    <polygon points="0,612 477,543 710,600 710,610 477,553 0,622" fill="var(--blue)"/>
    <polygon points="0,622 477,553 710,610 710,624 477,567 0,636" fill="var(--navy)"/>
    <polygon points="0,636 250,600 330,1134 0,1134" fill="var(--slate)"/>
    <polygon points="250,600 262,598 342,1134 330,1134" fill="var(--blue)"/>
    <circle cx="144" cy="672" r="118" fill="var(--navy)"/>
    <circle cx="144" cy="672" r="111" fill="var(--white)"/>
    <circle cx="144" cy="672" r="104" fill="var(--blue)"/>
    <rect x="0" y="1140" width="710" height="60" fill="var(--navy)"/>
  </svg>

  <header class="brand">
    <div class="brand-name"><span class="brand-mark"></span>Morville Law</div>
    <p class="brand-tagline">Steady counsel for every claim</p>
  </header>

  <div class="experience">
    <div class="over">OVER</div>
    <div class="years">20 YEARS</div>
    <div class="label">experience</div>
  </div>

  <h1 class="headline">
    <div class="line-1">Injured in an</div>
    <div class="line-2">accident?</div>
    <div class="line-3">Unhappy</div>
  </h1>

  <div class="results">We get<span class="caps">RESULTS!</span></div>

  <div class="recovered">
    <div class="small">Over millions</div>
    <div class="big">recovered</div>
  </div>

  <div class="contact">
    <div class="cta">CALL NOW</div>
    <div class="phone">(888) 514 - 2673</div>
    <div class="email">info@morvillelaw.com</div>
  </div>

  <ul class="credentials">
    <li>Prime Counsel</li>
    <li>Lexra 10.0</li>
    <li>Grand-Verdict dollars<br>barrister circle</li>
  </ul>

  <footer class="website">www.Morvillelaw.com</footer>
</main>
</body>
</html>
```